Health & Nutrition - Business Cards

Needs to look new-age, simple, and elegant. The cards are for my services/counsel in health and nutrition - which include mind, body, and soul. I would like to see something clean and simple but beautiful. Can have a plain background or with a pattern but I don't want it to take away from my contact details. Therefore, my info can be on the back of the card and a nice front design. I really like the flower of life symbol. The name of my business is called Willow Lantern.

Target Market(s)

Clients - men & women age 20-60. Adults, parents, teachers, sick individuals seeking nutrient counseling and dietary management.

Industry/Entity Type

Nutritionist

Contact Information for Business Card

Tomas Brindle
Cell: 345-582-7046
Email: tbrindle@mailvane.net

Colors
33a6d7
33b8a4
add136
ffffff
5c5c5c
f04a50
fbee3f
cedeed
85cae6

Requirements
Nice to have
• Maybe it can have some sort of sacred geometry as well, but not required. Nice to have the colors that I choose in the project but feel free to come up with your own use of colors. Thanks! =)

```html
<!DOCTYPE html>
<html lang="en">
<head>
<meta charset="utf-8">
<title>Willow Lantern – Business Cards</title>
<link rel="stylesheet" href="https://fonts.googleapis.com/css2?family=Noto+Serif+Display:wght@400;500&display=swap">
<style>
  :root {
    --ink: #5c5c5c;
    --paper: #ffffff;
    --red: #f04a50;
    --yellow: #fbee3f;
    --green: #add136;
    --teal: #33b8a4;
    --edge: #3a3a3a;
    --serif: "Noto Serif Display", Georgia, serif;
  }
  html, body {
    margin: 0;
    padding: 0;
    width: 901px;
    height: 1200px;
    overflow: hidden;
    background: var(--paper);
  }
  .sheet {
    position: relative;
    width: 901px;
    height: 1200px;
    font-family: var(--serif);
    color: var(--ink);
  }
  .card {
    position: absolute;
    left: 1px;
    width: 898px;
    height: 513px;
    box-sizing: border-box;
  }
  .card--front {
    top: 1px;
    border: 1px solid var(--edge);
    overflow: hidden;
  }
  .card--front svg { display: block; width: 100%; height: 100%; }
  .card--back {
    top: 685px;
    border: 1px solid #8a8a8a;
    background: var(--paper);
    overflow: hidden;
  }
  .back__info { position: absolute; left: 0; top: 0; width: 574px; height: 100%; }
  .back__panel {
    position: absolute;
    right: 0;
    top: 0;
    width: 323px;
    height: 100%;
    background: var(--ink);
  }
  .line {
    position: absolute;
    left: 32px;
    margin: 0;
    line-height: 1;
    white-space: nowrap;
    font-weight: 400;
  }
  .business-name { top: 32px; font-size: 57px; }
  .business-tagline { top: 90px; font-size: 23px; }
  .person-name { top: 308px; font-size: 57px; }
  .person-role { top: 366px; font-size: 25px; }
  .contact { font-size: 25px; }
  .contact--cell { top: 426px; }
  .contact--email { top: 464px; }
  .panel-name {
    position: absolute;
    left: 0;
    width: 100%;
    top: 210px;
    margin: 0;
    text-align: center;
    color: var(--paper);
    font-size: 36px;
    line-height: 1.15;
    font-weight: 400;
  }
  .front-name {
    font-family: var(--serif);
    font-size: 44px;
    fill: var(--paper);
  }
</style>
</head>
<body>
<main class="sheet">
  <section class="card card--front" aria-label="Card front">
    <svg viewBox="0 0 1052 601" preserveAspectRatio="none">
      <polygon class="tile tile--green" fill="var(--green)" points="0,0 301,300 526,525 599,601 0,601"/>
      <polygon class="tile tile--red" fill="var(--red)" points="0,0 599,0 301,300"/>
      <polygon class="tile tile--yellow" fill="var(--yellow)" points="599,0 1052,0 750,300 526,76"/>
      <polygon class="tile tile--teal" fill="var(--teal)" points="1052,0 1052,601 599,601 526,525 750,300"/>
      <polygon class="tile tile--center" fill="var(--ink)" points="526,76 750,300 526,525 301,300"/>
      <text class="front-name" x="526" y="300" text-anchor="middle" dominant-baseline="middle">Willow Lantern</text>
    </svg>
  </section>

  <section class="card card--back" aria-label="Card back">
    <div class="back__info">
      <h1 class="line business-name">Willow Lantern</h1>
      <p class="line business-tagline">Health &amp; Nutritions</p>
      <h2 class="line person-name">Tomas Brindle</h2>
      <p class="line person-role">Nutritionist</p>
      <p class="line contact contact--cell">Cell: 345-582-7046</p>
      <p class="line contact contact--email">Email: tbrindle@mailvane.net</p>
    </div>
    <div class="back__panel">
      <p class="panel-name">Willow<br>Lantern</p>
    </div>
  </section>
</main>
</body>
</html>
```